Presentation card Venture KELO - Tech Incubator from Perú

We need a Design to promote the incubator of technology Startups.
We are in Perú, we work with a string tech filter and develop enterprenurship competencies in the Startup team.
The card is to facilitators and staff memebers of VentureKELO.
We want a clear, modern, tech and agile Design.

We work to help New enterprises of technology here in Perú, we expect the candidates have a big competencies to Research and develop technological products.

We work using methodologies from QRB, Folmestry, Brakewell and Harrowgate univeesities. Our book base is the disciplina of enterpreneur.

We work events all year using diferent formats: Brightforge, Vorne price, OPRA Model Competition you can use these logros in your Design.

Set the name, role, email, cell phone number, address.

Example:
// Contact info section
Tobías Quiroveda
Swift Modeling Hub Manager
tobias.quiroveda@kelo-example.pe
(511) 999 000 417

// Address info section
VentureKELO
Technology-based business incubator
Av. Los Cedrales 884, Valdora
Lima - Perú
web: venture-kelo-example.org.pe
email: venture@kelo-example.pe
phone number: (511) 3926508 ext. 4418

// (optional)Lema section
Making happy using technology

// Social network section
facebook: venturekelooficial

Target Market(s)

Enterprenurship, CTO, Investors, Companies interested on open innovation services

Industry/Entity Type

Information Technology

Contact Information for Business Card

Name, Role, Email, Cell phone number

Colors

Designer to choose colors to be used in the design.

Requirements
Must have
• Logo forms and colors
Nice to have
• I add pictures of the leaders of incubator
Should not have
• No vertical designs

```html
<!DOCTYPE html>
<html lang="en">
<head>
<meta charset="utf-8">
<title>Venture KELO – Business Card</title>
<link rel="stylesheet" href="https://fonts.googleapis.com/css2?family=Arimo:wght@700&family=Open+Sans:wght@400;700&display=swap">
<style>
  :root {
    --brand-crimson: #c22c55;
    --ink: #2b2b2b;
    --paper: #ffffff;
  }
  html, body {
    margin: 0;
    padding: 0;
    width: 1000px;
    height: 1200px;
    overflow: hidden;
    background: var(--paper);
  }
  .card-sheet {
    display: block;
    width: 1000px;
    height: 1200px;
  }
  .card-outline { fill: none; stroke: var(--brand-crimson); stroke-width: 3; }
  .inner-frame { fill: none; stroke: var(--brand-crimson); stroke-width: 5; }
  .brand-band, .back-face { fill: var(--brand-crimson); }
  .title-rule { stroke: var(--brand-crimson); stroke-width: 5; }
  .brand-wordmark {
    font-family: "Open Sans", sans-serif;
    font-weight: 700;
    fill: var(--ink);
  }
  .brand-wordmark--reverse { fill: var(--paper); }
  .company-title {
    font-family: "Arimo", sans-serif;
    font-weight: 700;
    font-size: 41px;
    fill: var(--ink);
  }
  .person-name {
    font-family: "Open Sans", sans-serif;
    font-size: 32px;
    fill: var(--ink);
  }
  .person-role {
    font-family: "Open Sans", sans-serif;
    font-size: 25px;
    fill: var(--ink);
  }
  .contact-line {
    font-family: "Open Sans", sans-serif;
    font-size: 25px;
    fill: var(--paper);
  }
</style>
</head>
<body>
<svg class="card-sheet" viewBox="0 0 1000 1200" xmlns="http://www.w3.org/2000/svg">
  <!-- Front face -->
  <g class="card-front">
    <rect class="card-outline" x="3" y="3" width="995" height="552"/>
    <path class="inner-frame" d="M62 379 V142 Q160 150 185 110 Q198 85 201 56 H946 V379"/>
    <path class="brand-band" d="M59 379 H948 V381 A120 120 0 0 1 828 501 H59 Z"/>

    <text class="brand-wordmark" font-size="24">
      <tspan x="70" y="93">Venture</tspan>
      <tspan x="70" y="123">KELO</tspan>
    </text>

    <text class="company-title" x="540" y="155">VENTURE KELO</text>
    <line class="title-rule" x1="538" y1="178" x2="862" y2="178"/>

    <text class="person-name" x="121" y="271">XXXXXX XXXXXXX</text>
    <text class="person-role" x="121" y="315">Marketing Leader</text>

    <text class="contact-line" x="534" y="428">M<tspan dx="14">+000 00000000</tspan></text>
    <text class="contact-line" x="534" y="463">XXXXXX.XXXXXX@XXXX.com</text>
  </g>

  <!-- Back face -->
  <g class="card-back">
    <path class="back-face" d="M5 647 H998 V1001 A197 197 0 0 1 801 1198 H5 Z"/>
    <text class="brand-wordmark brand-wordmark--reverse" font-size="44" text-anchor="middle">
      <tspan x="496" y="915">Venture</tspan>
      <tspan x="496" y="967">KELO</tspan>
    </text>
  </g>
</svg>
</body>
</html>
```